Create a Big Data Website that is professional but has a creative flare to it.

I am after a modern business design for a company in the Big Data space however it still needs to have a wow value and something stand out from other corporate websites.
My competitors websites are to give you and idea of content:
www.flintavel.com
www.morvanti.com
www.quarlix4.com.au
www.tessadrine.com
I have uploaded my company Logo so you can use that to make sure it matches your theme.

Target Market(s)

Banks, Insurance Companies, Government, Gas and Energy Companies and Food Manufacturing.

Industry/Entity Type

Consulting

Coding

Coded - Design and coding required

Number of Pages Required

5+ page

Colors

Designer to choose colors to be used in the design.

Requirements
Must have
• Images, Diagrams around Big Data. Usage of information or graphs from sources like Pollwick are fine to use.
Nice to have
• Interactive design use mouse overs, change in text, highlighting information for clear focus.
Should not have
• Cluttered Pages of Informaiton

```html
<!DOCTYPE html>
<html lang="en">
<head>
<meta charset="utf-8">
<title>Stratalyn Consulting</title>
<link href="https://fonts.googleapis.com/css2?family=Open+Sans:ital,wght@0,300;0,400;0,600;0,700;0,800;1,400&display=swap" rel="stylesheet">
<style>
:root{
  --brand:#0b8bd6;
  --brand-dark:#16457a;
  --footer:#0f8edb;
  --footer-line:rgba(255,255,255,.35);
  --testimonial:#4aaee4;
  --ink:#333;
  --muted:#666;
  --soft:#f7f7f7;
  --white:#fff;
  --border:#dcdcdc;
}
*{box-sizing:border-box;margin:0;padding:0}
html,body{width:1200px;height:2786px;overflow:hidden}
body{font-family:"Open Sans",Arial,sans-serif;color:var(--ink);background:var(--white);position:relative}
a{color:inherit;text-decoration:none}

.site-header{height:105px;display:flex;align-items:center;justify-content:space-between;padding:0 98px 0 100px;box-shadow:0 2px 6px rgba(0,0,0,.08);position:relative;z-index:2;background:var(--white)}
.brand{display:flex;align-items:center;gap:12px}
.brand-mark{width:46px;height:46px;background:var(--brand);border-radius:4px}
.brand-name{font-weight:800;font-size:30px;color:var(--brand-dark);line-height:1}
.brand-name small{display:block;font-size:12px;font-weight:800;letter-spacing:1.3px;margin-top:3px}
.main-nav{display:flex;gap:40px;font-size:15px;align-items:center}
.main-nav .active{color:var(--brand)}

.hero{height:567px;position:relative;text-align:center;color:var(--white);
  background:radial-gradient(ellipse at 70% 55%,#7f8fb0 0%,transparent 45%),linear-gradient(135deg,#2b4f82 0%,#5777a8 45%,#1c3768 100%)}
.hero-inner{position:absolute;left:0;right:0;top:160px}
.hero h1{font-size:70px;font-weight:800;line-height:1;text-shadow:0 2px 6px rgba(0,0,0,.3)}
.hero p{font-size:32px;font-weight:300;margin-top:10px}
.btn-hero{display:inline-block;margin-top:28px;background:var(--brand);font-size:23px;padding:10px 22px}
.hero-arrow{position:absolute;top:240px}
.hero-arrow.prev{left:36px}.hero-arrow.next{right:36px}

.welcome{height:381px;text-align:center;padding-top:65px}
.section-title{font-size:34px;font-weight:300;color:#444}
.welcome .section-title{color:var(--brand);font-weight:400}
.welcome p{width:820px;margin:22px auto 0;font-size:13.5px;line-height:27px;color:var(--muted)}

.services{height:559px;background:var(--soft);text-align:center;padding-top:50px}
.services .intro{width:840px;margin:20px auto 0;font-size:13.5px;line-height:27px;color:var(--muted)}
.service-list{display:flex;justify-content:center;gap:88px;margin-top:48px}
.service{width:122px;display:flex;flex-direction:column;align-items:center}
.service h3{font-size:14.5px;font-weight:600;margin-top:18px;white-space:nowrap}
.service p{font-size:11px;line-height:20px;color:#444;margin-top:12px;width:170px;height:40px}
.btn-read{margin-top:18px;background:var(--brand);color:var(--white);font-size:13px;font-weight:600;width:120px;height:37px;line-height:37px}

.testimonials{height:488px;text-align:center;color:var(--white);position:relative;
  background:radial-gradient(ellipse at 50% 65%,#8fd0f2 0%,transparent 55%),var(--testimonial)}
.testimonials .section-title{color:var(--white);padding-top:58px;font-weight:300}
.quote{width:840px;margin:28px auto 0;font-style:italic;font-size:12.5px;line-height:27px;position:relative}
.quote-mark{position:absolute;font-size:60px;font-style:normal;opacity:.6;line-height:1}
.quote-mark.open{left:-40px;top:-6px}.quote-mark.close{right:-40px;bottom:-40px}
.avatar{width:140px;height:140px;border-radius:50%;border:7px solid var(--white);margin:22px auto 0;background:linear-gradient(180deg,#e9eef3 0%,#9aa9b8 100%)}
.client-name{font-size:15px;letter-spacing:1px;margin-top:16px}

.partners{height:345px;text-align:center;padding-top:65px;position:relative}
.partner-row{display:flex;justify-content:center;gap:15px;margin-top:43px}
.partner{width:155px;height:93px;border:1px solid var(--border);display:flex;align-items:center;justify-content:center;gap:8px;font-size:13px;font-weight:600;color:#445}
.partner i{width:14px;height:14px;background:#8aa;display:block}
.partner-arrow{position:absolute;top:197px}
.partner-arrow.prev{left:52px}.partner-arrow.next{right:52px}

.site-footer{height:341px;background:var(--footer);color:var(--white);padding:40px 98px 0;position:relative}
.footer-cols{display:flex}
.footer-col h4{font-size:17px;font-weight:600;margin-bottom:18px}
.links{width:362px;display:flex}
.links ul{list-style:none;font-size:13.5px;line-height:31.5px;width:182px}
.contact{width:312px;font-size:14.5px;line-height:31px}
.contact li{list-style:none;display:flex;align-items:center;gap:10px}
.newsletter{font-size:13.5px}
.signup{display:flex;margin-top:14px}
.signup span{width:220px;height:40px;background:var(--white);color:#999;font-size:13px;line-height:40px;padding-left:15px}
.signup b{width:106px;height:40px;background:var(--brand-dark);font-size:13px;font-weight:400;line-height:40px;text-align:center}
.social{display:flex;gap:11px;margin-top:16px}
.social i{width:38px;height:38px;border-radius:50%;background:var(--white);display:block}
.footer-bottom{position:absolute;left:98px;right:98px;top:270px;border-top:1px solid var(--footer-line);padding-top:16px;font-size:13px;display:flex;justify-content:space-between}
</style>
</head>
<body>

<header class="site-header">
  <div class="brand"><span class="brand-mark"></span><span class="brand-name">Stratalyn<small>CONSULTING SERVICES</small></span></div>
  <nav class="main-nav">
    <a class="active">Home</a><a>About Us</a><a>Services</a><a>Events</a><a>Our Partners</a><a>Contact Us</a>
    <svg width="14" height="14" viewBox="0 0 14 14"><circle cx="6" cy="6" r="4.5" fill="none" stroke="#0b8bd6" stroke-width="2"/><line x1="9.5" y1="9.5" x2="13" y2="13" stroke="#0b8bd6" stroke-width="2"/></svg>
  </nav>
</header>

<section class="hero" role="img" aria-label="Photo of hands typing on a laptop with data charts and network lines overlaid">
  <svg class="hero-arrow prev" width="16" height="34"><polyline points="14,2 2,17 14,32" fill="none" stroke="rgba(255,255,255,.6)" stroke-width="2"/></svg>
  <svg class="hero-arrow next" width="16" height="34"><polyline points="2,2 14,17 2,32" fill="none" stroke="rgba(255,255,255,.6)" stroke-width="2"/></svg>
  <div class="hero-inner">
    <h1>Stratalyn Consulting</h1>
    <p>We provide services related to Big Data.</p>
    <a class="btn-hero">Learn More &nbsp;›</a>
  </div>
</section>

<section class="welcome">
  <h2 class="section-title">WELCOME TO STRATALYN CONSULTING</h2>
  <p>Lorem ipsum dolor sit amet, consectetur adipiscing elit, sed do eiusmod tempor incididunt ut labore et dolore magna aliqua. Ut enim ad minim veniam, quis nostrud exercitation ullamco laboris nisi ut aliquip ex ea commodo consequat. Duis aute irure dolor in reprehenderit in voluptate velit esse cillum dolore eu fugiat nulla pariatur.</p>
  <p>Sed ut perspiciatis unde omnis iste natus error sit voluptatem accusantium doloremque laudantium, totam rem aperiam, eaque ipsa quae ab illo inventore veritatis et quasi architecto beatae vitae dicta sunt explicabo.</p>
</section>

<section class="services">
  <h2 class="section-title">OUR SERVICES</h2>
  <p class="intro">At vero eos et accusamus et iusto odio dignissimos ducimus qui blanditiis praesentium voluptatum deleniti atque corrupti quos dolores et quas molestias excepturi sint occaecati cupiditate non provident.</p>
  <div class="service-list">
    <div class="service">
      <svg width="122" height="104" viewBox="0 0 122 104"><polygon points="32,4 90,4 118,52 90,100 32,100 4,52" fill="#fff" stroke="#0b8bd6" stroke-width="8"/><g fill="#0b8bd6"><rect x="42" y="60" width="7" height="12"/><rect x="52" y="54" width="7" height="18"/><rect x="62" y="48" width="7" height="24"/><rect x="72" y="40" width="7" height="32"/></g><polyline points="40,52 56,42 66,46 80,32" fill="none" stroke="#0b8bd6" stroke-width="3"/></svg>
      <h3>Trends &amp; Predictions</h3>
      <p>Predictions for 2017: Innovation Brings Digital Disruption</p>
      <a class="btn-read">READ MORE</a>
    </div>
    <div class="service">
      <svg width="122" height="104" viewBox="0 0 122 104"><polygon points="32,4 90,4 118,52 90,100 32,100 4,52" fill="#fff" stroke="#0b8bd6" stroke-width="8"/><rect x="40" y="34" width="40" height="28" fill="none" stroke="#0b8bd6" stroke-width="3"/><line x1="60" y1="62" x2="60" y2="70" stroke="#0b8bd6" stroke-width="3"/><line x1="50" y1="71" x2="70" y2="71" stroke="#0b8bd6" stroke-width="3"/><circle cx="72" cy="54" r="7" fill="#fff" stroke="#0b8bd6" stroke-width="3"/><line x1="77" y1="59" x2="84" y2="66" stroke="#0b8bd6" stroke-width="3"/><rect x="46" y="46" width="4" height="10" fill="#0b8bd6"/><rect x="53" y="42" width="4" height="14" fill="#0b8bd6"/></svg>
      <h3>Data Analytics</h3>
      <p>Advance Your Business with Advanced Analytics</p>
      <a class="btn-read">READ MORE</a>
    </div>
    <div class="service">
      <svg width="122" height="104" viewBox="0 0 122 104"><polygon points="32,4 90,4 118,52 90,100 32,100 4,52" fill="#fff" stroke="#0b8bd6" stroke-width="8"/><path d="M44 64 a10 10 0 0 1 2-20 a15 15 0 0 1 28-4 a12 12 0 0 1 4 24 z" fill="none" stroke="#0b8bd6" stroke-width="3"/><line x1="61" y1="70" x2="61" y2="48" stroke="#0b8bd6" stroke-width="3"/><polyline points="54,55 61,48 68,55" fill="none" stroke="#0b8bd6" stroke-width="3"/></svg>
      <h3>Cloud Computing</h3>
      <p>5 Ways Cloud Can Transform Your Business</p>
      <a class="btn-read">READ MORE</a>
    </div>
    <div class="service">
      <svg width="122" height="104" viewBox="0 0 122 104"><polygon points="32,4 90,4 118,52 90,100 32,100 4,52" fill="#fff" stroke="#0b8bd6" stroke-width="8"/><g stroke="#0b8bd6" stroke-width="2.5"><line x1="61" y1="52" x2="61" y2="34"/><line x1="61" y1="52" x2="61" y2="70"/><line x1="61" y1="52" x2="42" y2="52"/><line x1="61" y1="52" x2="80" y2="52"/><line x1="61" y1="52" x2="48" y2="39"/><line x1="61" y1="52" x2="74" y2="65"/></g><g fill="#0b8bd6"><circle cx="61" cy="52" r="7"/><circle cx="61" cy="33" r="4"/><circle cx="61" cy="71" r="4"/><circle cx="41" cy="52" r="4"/><circle cx="81" cy="52" r="4"/><circle cx="47" cy="38" r="4"/><circle cx="75" cy="66" r="4"/></g></svg>
      <h3>Internet of Things</h3>
      <p>Why IoT? Harness the Power of Connected Things</p>
      <a class="btn-read">READ MORE</a>
    </div>
    <div class="service">
      <svg width="122" height="104" viewBox="0 0 122 104"><polygon points="32,4 90,4 118,52 90,100 32,100 4,52" fill="#fff" stroke="#0b8bd6" stroke-width="8"/><rect x="41" y="34" width="40" height="36" fill="none" stroke="#0b8bd6" stroke-width="3"/><circle cx="61" cy="47" r="7" fill="#0b8bd6"/><path d="M47 68 q14 -18 28 0 z" fill="#0b8bd6"/></svg>
      <h3>Cio Leadership</h3>
      <p>Insights to Help CIOs Lead, Transform, and Grow</p>
      <a class="btn-read">READ MORE</a>
    </div>
  </div>
</section>

<section class="testimonials" role="img" aria-label="Blue background of flowing binary digits">
  <h2 class="section-title">CLIENT TESTIMONIALS</h2>
  <blockquote class="quote">
    <span class="quote-mark open">“</span>
    But I must explain to you how all this mistaken idea of denouncing pleasure and praising pain was born and I will give you a complete account of the system, and expound the actual teachings of the great explorer of the truth, the master-builder of human happiness. No one rejects, dislikes, or avoids pleasure itself, because it is pleasure, but because those who do not know how to pursue pleasure rationally encounter consequences that are extremely painful
    <span class="quote-mark close">”</span>
  </blockquote>
  <div class="avatar" role="img" aria-label="Portrait photo of a businessman at a laptop"></div>
  <p class="client-name">ASSUMENDA EST</p>
</section>

<section class="partners">
  <h2 class="section-title">OUR STRATEGIC PARTNERS</h2>
  <svg class="partner-arrow prev" width="14" height="28"><polyline points="12,2 2,14 12,26" fill="none" stroke="#bbb" stroke-width="3"/></svg>
  <svg class="partner-arrow next" width="14" height="28"><polyline points="2,2 12,14 2,26" fill="none" stroke="#bbb" stroke-width="3"/></svg>
  <div class="partner-row">
    <div class="partner"><i></i>Harbourline</div>
    <div class="partner"><i></i>Wexford Holdings</div>
    <div class="partner"><i></i>Corvani Bank</div>
    <div class="partner"><i></i>Telvaro Networks</div>
    <div class="partner"><i></i>Lendwise</div>
    <div class="partner"><i></i>Ordovan Mining</div>
  </div>
</section>

<footer class="site-footer">
  <div class="footer-cols">
    <div class="footer-col">
      <h4>QUICK LINKS</h4>
      <div class="links">
        <ul><li>Home</li><li>About Us</li><li>Services</li><li>Events</li><li>Our Partners</li></ul>
        <ul><li>Terms of Service</li><li>Privacy Policy</li><li>FAQ's</li></ul>
      </div>
    </div>
    <div class="footer-col contact">
      <h4>CONTACT INFO</h4>
      <ul>
        <li>Stratalyn Consulting., Street Name,</li>
        <li>Address, Country, Pin Code.</li>
        <li><svg width="14" height="14" viewBox="0 0 14 14"><path d="M3 1 l3 3 -2 2 q2 3 4 4 l2-2 3 3 -2 2 q-7 0 -11-10 z" fill="#fff"/></svg>(+01) 555-01827</li>
        <li><svg width="14" height="11" viewBox="0 0 14 11"><rect width="14" height="11" fill="#fff"/><polyline points="0,0 7,6 14,0" fill="none" stroke="#0f8edb" stroke-width="1.5"/></svg>hello@stratalynmail.com</li>
      </ul>
    </div>
    <div class="footer-col newsletter">
      <h4>SIGN UP FOR NEWSLETTERS</h4>
      <p>Please sign up here for latest news</p>
      <div class="signup"><span>EMAIL ADDRESS</span><b>SUBSCRIBE</b></div>
      <div class="social"><i></i><i></i><i></i><i></i></div>
    </div>
  </div>
  <div class="footer-bottom"><span>© 2017 STRATALYN CONSULTING.. All right reserved . Term of Use</span></div>
</footer>

</body>
</html>
```